Business Card/Letterhead Design

We have our Logo, we simply need it cleaned up. Along with a letterhead design. It's pretty simple really.
Instead of the "Corporation" beside the logo. We need it to say "Limited" just under the logo between the "F" and the "Y"
The letter head has to have our address. 4375 Calverton Road Mississauga, ON L4W 2K7 Canada
Updates
Reason: I have been called out of town until Monday of next week.
Industry/Entity Type
Business
Contact Information for Business Card
4375 Calverton Road Mississauga, ON L4W 2K7 Canada
Look and feel
Each slider illustrates characteristics of the customer's brand and the style your logo design should communicate.

```html
<!DOCTYPE html>
<html lang="en">
<head>
<meta charset="UTF-8">
<title>Northvale Limited Letterhead</title>
<link href="https://fonts.googleapis.com/css2?family=Open+Sans:wght@400;600;700&display=swap" rel="stylesheet">
<style>
  :root {
    --brand: #4b3f9e;
    --ink: #2b2b2b;
    --muted: #555555;
    --rule-grey: #8a8a8a;
    --paper: #ffffff;
  }
  * { margin: 0; padding: 0; box-sizing: border-box; }
  html, body {
    width: 800px;
    height: 1200px;
    overflow: hidden;
    background: var(--paper);
    font-family: "Open Sans", Arial, sans-serif;
  }
  .letterhead {
    position: relative;
    width: 800px;
    height: 1200px;
    background: var(--paper);
  }
  .brand {
    position: absolute;
    left: 44px;
    top: 40px;
    display: flex;
    align-items: center;
    gap: 14px;
  }
  .brand-dot {
    width: 34px;
    height: 34px;
    border-radius: 50%;
    background: var(--brand);
  }
  .brand-name {
    font-size: 38px;
    font-weight: 600;
    color: var(--brand);
    letter-spacing: 0.5px;
    line-height: 1;
  }
  .contact {
    position: absolute;
    right: 48px;
    top: 26px;
    text-align: right;
  }
  .contact-name {
    font-size: 19px;
    font-weight: 700;
    color: var(--ink);
    line-height: 1.2;
  }
  .contact-title {
    font-size: 11px;
    color: var(--brand);
    margin-top: 2px;
  }
  .contact-line {
    font-size: 10.5px;
    color: var(--muted);
    margin-top: 4px;
  }
  .contact-title + .contact-line { margin-top: 16px; }
  .rule {
    position: absolute;
    left: 0;
    width: 800px;
  }
  .rule span { display: block; height: 2px; }
  .rule .grey { background: var(--rule-grey); }
  .rule .brand-line { background: var(--brand); margin-top: 3px; height: 3px; }
  .rule-top { top: 120px; }
  .rule-bottom { top: 1130px; }
  .footer {
    position: absolute;
    left: 0;
    top: 1150px;
    width: 800px;
    text-align: center;
    font-size: 11px;
    line-height: 1.5;
  }
  .footer-address { color: var(--ink); }
  .footer-web { color: var(--brand); }
</style>
</head>
<body>
  <div class="letterhead">
    <div class="brand">
      <div class="brand-dot"></div>
      <div class="brand-name">Northvale Limited</div>
    </div>

    <div class="contact">
      <div class="contact-name">Daniel Morrow</div>
      <div class="contact-title">Managing Director</div>
      <div class="contact-line">T: 905-555-0142</div>
      <div class="contact-line">E: info@northvale.ca</div>
    </div>

    <div class="rule rule-top"><span class="grey"></span><span class="brand-line"></span></div>

    <div class="rule rule-bottom"><span class="grey"></span><span class="brand-line"></span></div>

    <div class="footer">
      <div class="footer-address">4375 Calverton Road Mississauga, ON L4W 2K7 Canada</div>
      <div class="footer-web">www.northvale.ca</div>
    </div>
  </div>
</body>
</html>
```